Vodka bottle label for premium caribbean market

Label design for a Vodka bottle
Vodka name is 742 Vodka
General colors desired are red and blue
This is a premium vodka product that will be made and distributed in the Caribbean
The art in the background are used in religious celebrations and need to be incorporated
The 742 Vodka design is what I personally created and want to follow a similar art design
Logo should say 742 Vodka

Reason: I was out on leave for personal reasons but ready to make a decision as soon as possible.

Target Market(s)

Premium vodka

Industry/Entity Type

Product

Logo Text

742 Vodka

Font styles to use
Other font styles liked:
• French Script MT

Colors
ec1f27
3176b5

Requirements
Must have
• Incorporate the name 742 Vodka
• Incorporate the 4 art designs as attached
• Font type is provided as an example
• 742 = French Script MT
• Vodka = Footlight MT light
Nice to have
• N/A
Should not have
• N/A

```html
<!DOCTYPE html>
<html lang="en">
<head>
<meta charset="utf-8">
<title>742 Vodka Label</title>
<link rel="stylesheet" href="https://fonts.googleapis.com/css2?family=Cinzel:wght@400&display=swap">
<style>
  :root {
    --vodka-red: #ec1f27;
    --caribbean-blue: #3176b5;
    --brush-blue: #1f5fb0;
    --label-white: #ffffff;
    --page-bg: #f2f2f2;
    --ornament-tone: #cfcfcf;
  }
  html, body {
    margin: 0;
    padding: 0;
    width: 1200px;
    height: 1098px;
    overflow: hidden;
    background: var(--page-bg);
  }
  .canvas {
    position: relative;
    width: 1200px;
    height: 1098px;
  }
  .label {
    position: absolute;
    left: 327px;
    top: 29px;
    width: 547px;
    height: 1041px;
    background: var(--label-white);
    overflow: hidden;
  }
  .brush-mark {
    position: absolute;
    left: 67px;
    top: 14px;
    width: 361px;
    height: 193px;
  }
  .brand-mark {
    position: absolute;
    left: 67px;
    top: 48px;
    width: 361px;
    text-align: center;
    font-family: "Cinzel", serif;
    font-weight: 400;
    color: var(--label-white);
    line-height: 1;
  }
  .brand-mark .brand-number {
    display: block;
    font-size: 62px;
  }
  .brand-mark .brand-word {
    display: block;
    margin-top: 8px;
    font-size: 24px;
    letter-spacing: 1px;
  }
  .veve {
    position: absolute;
    background: var(--ornament-tone);
    border-radius: 6px;
  }
  .veve-top-left { left: 92px; top: 335px; width: 205px; height: 115px; }
  .veve-mid-right { left: 240px; top: 444px; width: 189px; height: 140px; }
  .veve-low-left { left: 120px; top: 600px; width: 140px; height: 152px; }
  .veve-bottom-right { left: 244px; top: 703px; width: 180px; height: 168px; }
  .stacked-number {
    position: absolute;
    left: 184px;
    width: 160px;
    text-align: center;
    font-family: "Cinzel", serif;
    font-weight: 400;
    font-size: 205px;
    line-height: 1;
    color: var(--vodka-red);
  }
  .digit-one { top: 328px; }
  .digit-two { top: 513px; }
  .digit-three { top: 702px; }
  .product-word {
    position: absolute;
    left: 60px;
    top: 926px;
    width: 460px;
    text-align: center;
    font-family: "Cinzel", serif;
    font-weight: 400;
    font-size: 92px;
    line-height: 1;
    letter-spacing: 22px;
    color: var(--vodka-red);
  }
</style>
</head>
<body>
<main class="canvas">
  <section class="label">
    <svg class="brush-mark" viewBox="0 0 361 193" role="img" aria-label="Blue painted brush stroke behind the brand name">
      <defs>
        <linearGradient id="brushTone" x1="0" y1="0" x2="1" y2="1">
          <stop offset="0" stop-color="#2a6cc0"/>
          <stop offset="1" stop-color="#1a55a6"/>
        </linearGradient>
      </defs>
      <path d="M10 70 C40 30 120 35 180 20 C240 8 300 15 330 60 C355 95 350 140 300 150 C250 165 200 178 140 170 C80 165 30 150 20 120 C5 100 0 85 10 70 Z" fill="url(#brushTone)"/>
    </svg>
    <div class="brand-mark">
      <span class="brand-number">742</span>
      <span class="brand-word">VODKA</span>
    </div>

    <div class="veve veve-top-left" role="img" aria-label="Black line-drawn ceremonial veve symbol"></div>
    <div class="veve veve-mid-right" role="img" aria-label="Black line-drawn ceremonial veve symbol with lattice"></div>
    <div class="veve veve-low-left" role="img" aria-label="Black line-drawn ceremonial veve symbol with cross"></div>
    <div class="veve veve-bottom-right" role="img" aria-label="Black line-drawn ceremonial veve symbol with circles"></div>

    <div class="stacked-number digit-one">7</div>
    <div class="stacked-number digit-two">4</div>
    <div class="stacked-number digit-three">2</div>

    <div class="product-word">VODKA</div>
  </section>
</main>
</body>
</html>
```